Briefpapier und Visitenkarten
Zielgruppe
Das Design soll Herren im mittleren bis hohen Alter ansprechen.
Aufgabenstellung
Benötigt wird ein Briefpapier für die Koresspondenz und die Rechnungen. Ein Logo ist vorhanden und muss ins Briefpapier und auf die Visitenkarten einbebunden werden.

```html
<!DOCTYPE html>
<html lang="de">
<head>
<meta charset="utf-8">
<title>Visitenkarte – alpen data partner</title>
<link rel="stylesheet" href="https://fonts.googleapis.com/css2?family=Poppins:wght@300;600&display=swap">
<style>
  :root {
    --brand-red: #c0000f;
    --ink: #1a1a1a;
    --paper: #ffffff;
    --backdrop: #ececec;
    --card-edge: #9a9a9a;
  }
  * { box-sizing: border-box; margin: 0; padding: 0; }
  html, body {
    width: 854px; height: 1200px; overflow: hidden;
    background: var(--backdrop);
    font-family: "Poppins", sans-serif;
  }
  .canvas { position: relative; width: 854px; height: 1200px; }
  .card {
    position: absolute; left: 98px; width: 661px; height: 426px;
    background: var(--paper);
    border: 1px solid var(--card-edge);
    overflow: hidden;
  }
  .card--front { top: 105px; }
  .card--back { top: 644px; }
  .card__swoosh { position: absolute; inset: 0; width: 100%; height: 100%; }
  .card__swoosh path { fill: var(--brand-red); }

  .wordmark {
    position: absolute; display: flex; align-items: center;
    color: var(--brand-red); font-weight: 600; white-space: nowrap;
    letter-spacing: -0.01em;
  }
  .wordmark__dot { border-radius: 50%; background: var(--brand-red); flex: none; }
  .wordmark--small { top: 22px; right: 38px; font-size: 22px; gap: 8px; }
  .wordmark--small .wordmark__dot { width: 16px; height: 16px; }
  .wordmark--large {
    top: 50%; left: 50%; transform: translate(-50%, -50%);
    font-size: 42px; gap: 14px;
  }
  .wordmark--large .wordmark__dot { width: 30px; height: 30px; }

  .contact { position: absolute; left: 119px; top: 68px; }
  .contact__name { color: var(--brand-red); font-weight: 600; font-size: 22px; line-height: 1.2; }
  .contact__address {
    margin-top: 38px; color: var(--ink); font-weight: 300;
    font-size: 22px; line-height: 33px;
  }
  .contact__online {
    margin-top: 32px; color: var(--brand-red); font-weight: 600;
    font-size: 20px; line-height: 34px;
  }
</style>
</head>
<body>
<main class="canvas">
  <section class="card card--front">
    <svg class="card__swoosh" viewBox="0 0 661 426" preserveAspectRatio="none" aria-hidden="true">
      <path d="M0 118 C 30 330, 170 422, 440 426 L 0 426 Z"/>
    </svg>
    <div class="wordmark wordmark--small"><span class="wordmark__dot"></span>alpen data partner</div>
    <div class="contact">
      <p class="contact__name">Lukas Brenner</p>
      <p class="contact__address">Lindenweg 14<br>52318 Talheim<br>Tel: 0341 57 19 86</p>
      <p class="contact__online">info@alpen-data.de<br>www.alpen-data-partner.de</p>
    </div>
  </section>

  <section class="card card--back">
    <svg class="card__swoosh" viewBox="0 0 661 426" preserveAspectRatio="none" aria-hidden="true">
      <path d="M0 103 C 30 320, 160 420, 420 426 L 0 426 Z"/>
    </svg>
    <div class="wordmark wordmark--large"><span class="wordmark__dot"></span>alpen data partner</div>
  </section>
</main>
</body>
</html>
```